PowerPoint design MervoSan

We need a PowerPoint set-up based upon our existing logo (see joint file)
Our company is operating in the health care and life science sector. We are mainly focussing on international business

Target Market(s)

International

Industry/Entity Type

health care and life sciences

Requirements
Must have
• Logos as added

```html
<!DOCTYPE html>
<html lang="en">
<head>
<meta charset="utf-8">
<title>MervoSan presentation template</title>
<link rel="stylesheet" href="https://fonts.googleapis.com/css2?family=Poppins:wght@400;600;700;800&display=swap">
<style>
  :root {
    --navy: #0b4f86;
    --green: #58b947;
    --orange: #ea6549;
    --yellow: #f5b720;
    --ink: #1d1d1d;
    --photo-deep: #1c2f86;
    --photo-light: #5d74b6;
    --white: #ffffff;
  }
  html, body {
    margin: 0;
    width: 1200px;
    height: 900px;
    overflow: hidden;
    background: var(--white);
    font-family: "Poppins", sans-serif;
  }
  .deck { position: relative; width: 1200px; height: 900px; }
  .slide {
    position: absolute;
    width: 512px;
    height: 384px;
    background: var(--white);
    box-shadow: 0 6px 28px rgba(0, 0, 0, 0.14);
    overflow: hidden;
  }
  .slide svg { display: block; width: 100%; height: 100%; }
  .slide--cover { left: 55px; top: 48px; }
  .slide--projects { left: 608px; top: 48px; }
  .slide--chart { left: 59px; top: 467px; }
  .slide--contact { left: 609px; top: 467px; }
  text { font-family: "Poppins", sans-serif; }
  .fill-navy { fill: var(--navy); }
  .fill-green { fill: var(--green); }
  .fill-white { fill: var(--white); }
  .heading { fill: var(--green); font-weight: 700; font-size: 24px; }
  .body-copy { fill: var(--ink); font-size: 14.5px; }
  .paragraph { fill: var(--ink); font-size: 14px; }
  .icon { fill: none; stroke: var(--green); stroke-width: 2.4; stroke-linecap: round; stroke-linejoin: round; }
  .icon-disc { fill: var(--white); filter: drop-shadow(0 2px 6px rgba(60, 80, 200, 0.35)); }
</style>
</head>
<body>
<main class="deck">

  <!-- Cover -->
  <section class="slide slide--cover">
    <svg viewBox="0 0 935 700" xmlns="http://www.w3.org/2000/svg">
      <defs>
        <linearGradient id="cellTone" x1="0" y1="0" x2="1" y2="1">
          <stop offset="0" stop-color="#2a3a96"/>
          <stop offset="0.5" stop-color="var(--photo-deep)"/>
          <stop offset="1" stop-color="#0d1550"/>
        </linearGradient>
      </defs>
      <polygon points="110,0 600,0 325,700 0,700 0,250" fill="url(#cellTone)" role="img" aria-label="Microscopic blue cells with a molecule network overlay"/>
      <polygon class="fill-green" points="0,0 92,0 0,232"/>
      <polygon class="fill-green" points="600,0 648,0 595,200 548,200"/>
      <polygon class="fill-green" points="648,0 693,0 640,200 595,200"/>
      <polygon class="fill-navy" points="662,162 935,162 935,200 647,200"/>
      <line x1="560" y1="200" x2="362" y2="700" stroke="var(--navy)" stroke-width="7"/>
      <circle class="fill-green" cx="540" cy="578" r="18"/>
      <text x="575" y="596" class="fill-navy" font-size="56" font-weight="600">MervoSan</text>
    </svg>
  </section>

  <!-- Project timeline -->
  <section class="slide slide--projects">
    <svg viewBox="0 0 935 700" xmlns="http://www.w3.org/2000/svg">
      <rect class="fill-navy" x="0" y="0" width="285" height="700"/>
      <circle class="fill-white" cx="293" cy="350" r="160"/>
      <text class="fill-white" font-size="66" font-weight="800" transform="translate(85 345) rotate(-90)" text-anchor="middle">Your project</text>
      <circle class="fill-green" cx="230" cy="350" r="10"/>
      <text x="250" y="361" class="fill-navy" font-size="30" font-weight="600">MervoSan</text>
      <path d="M285,100 A250,250 0 0 1 285,600" fill="none" stroke="var(--navy)" stroke-width="2.5"/>

      <g>
        <circle class="icon-disc" cx="335" cy="115" r="29"/>
        <rect class="icon" x="325" y="102" width="20" height="26" rx="2"/>
        <path class="icon" d="M329,110h12M329,115h12M329,120h12"/>
        <circle class="icon-disc" cx="450" cy="168" r="29"/>
        <path class="icon" d="M440,158v22h20v-22M444,170h6v8"/>
        <circle class="icon-disc" cx="523" cy="282" r="29"/>
        <path class="icon" d="M517,292h12M518,287c-8-6-6-20,5-20s13,14,5,20"/>
        <circle class="icon-disc" cx="523" cy="418" r="29"/>
        <circle cx="512" cy="417" r="4" fill="var(--green)"/><circle cx="533" cy="408" r="4" fill="var(--green)"/><circle cx="530" cy="428" r="4" fill="var(--green)"/>
        <path class="icon" d="M512,417l21-9M512,417l18,11"/>
        <circle class="icon-disc" cx="450" cy="533" r="29"/>
        <circle class="icon" cx="450" cy="527" r="8"/><path class="icon" d="M450,535v12"/>
        <circle class="icon-disc" cx="335" cy="590" r="29"/>
        <path class="icon" d="M327,578v8l-6,14h16l-6-14v-8M339,576v24h8v-24"/>
      </g>

      <g>
        <text x="393" y="70" class="heading">Your project</text>
        <text x="393" y="90" class="body-copy">Lorem ipsum dolor sit amet, consectetuer adipiscing</text>
        <text x="393" y="108" class="body-copy">elit, sed diam nonummy nibh</text>
        <text x="507" y="164" class="heading">Your project</text>
        <text x="507" y="184" class="body-copy">Lorem ipsum dolor sit amet, consectetuer adipiscing</text>
        <text x="507" y="202" class="body-copy">elit, sed diam nonummy nibh</text>
        <text x="572" y="282" class="heading">Your project</text>
        <text x="572" y="302" class="body-copy">Lorem ipsum dolor sit amet, consectetuer</text>
        <text x="572" y="320" class="body-copy">adipiscing elit, sed diam nonummy nibh</text>
        <text x="576" y="427" class="heading">Your project</text>
        <text x="576" y="447" class="body-copy">Lorem ipsum dolor sit amet, consectetuer</text>
        <text x="576" y="465" class="body-copy">adipiscing elit, sed diam nonummy nibh</text>
        <text x="505" y="538" class="heading">Your project</text>
        <text x="505" y="558" class="body-copy">Lorem ipsum dolor sit amet, consectetuer adipiscing</text>
        <text x="505" y="576" class="body-copy">elit, sed diam nonummy nibh</text>
        <text x="373" y="633" class="heading">Your project</text>
        <text x="373" y="653" class="body-copy">Lorem ipsum dolor sit amet, consectetuer adipiscing</text>
        <text x="373" y="671" class="body-copy">elit, sed diam nonummy nibh</text>
      </g>
    </svg>
  </section>

  <!-- Chart slide -->
  <section class="slide slide--chart">
    <svg viewBox="0 0 935 700" xmlns="http://www.w3.org/2000/svg">
      <polygon class="fill-navy" points="8,0 935,0 935,118 280,118 98,92"/>
      <polygon class="fill-green" points="52,0 232,0 350,118 170,118"/>
      <text x="162" y="90" class="fill-white" font-size="68" font-weight="800">01</text>
      <text x="892" y="80" class="fill-white" font-size="40" font-weight="800" text-anchor="end">SUB TITLE</text>

      <g stroke="var(--white)" stroke-width="5">
        <path fill="var(--navy)" d="M350,358 A120,120 0 0 1 118.7,403 L194.8,372.2 A38,38 0 0 0 268,358 Z"/>
        <path fill="var(--yellow)" d="M118.7,403 A120,120 0 0 1 221.6,238.2 L227.3,320.1 A38,38 0 0 0 194.8,372.2 Z"/>
        <path fill="var(--orange)" d="M221.6,238.2 A120,120 0 0 1 350,358 L268,358 A38,38 0 0 0 227.3,320.1 Z"/>
      </g>
      <circle cx="230" cy="358" r="35" fill="var(--white)" stroke="#8a8a8a" stroke-width="3"/>
      <path d="M244,232 L250,204 H270" fill="none" stroke="var(--orange)" stroke-width="1.5"/>
      <text x="280" y="212" fill="var(--orange)" font-size="21">36%</text>
      <path d="M70,358 H100" fill="none" stroke="var(--yellow)" stroke-width="1.5"/>
      <text x="20" y="366" fill="var(--yellow)" font-size="21">30%</text>
      <path d="M252,482 L258,506 H278" fill="none" stroke="var(--navy)" stroke-width="1.5"/>
      <text x="283" y="514" fill="var(--navy)" font-size="21">44%</text>

      <g class="paragraph">
        <text x="430" y="218"><tspan x="477">Lorem ipsum dolor sit amet, consectetuer adipiscing</tspan><tspan x="430" dy="18.7">elit, sed diam nonummy nibh euismod tincidunt ut laoreet</tspan><tspan x="430" dy="18.7">dolore magna aliquam erat volutpat. Ut wisi enim ad minim</tspan><tspan x="430" dy="18.7">veniam, quis nostrud exerci tation</tspan></text>
        <text x="430" y="311"><tspan x="430">ullamcorper suscipit lobortis nisl ut aliquip ex ea commodo</tspan><tspan x="430" dy="18.7">consequat. Duis autem vel eum iriure dolor in hendrerit in</tspan><tspan x="430" dy="18.7">vulputate velit esse molestie consequat, vel illum dolore eu</tspan><tspan x="430" dy="18.7">feugiat nulla facilisis at vero eros et accumsan et iusto odio</tspan><tspan x="430" dy="18.7">dignissim qui blandit praesent luptatum zzril delenit augue</tspan><tspan x="430" dy="18.7">duis dolore te feugait nulla facilisi.</tspan></text>
        <text x="430" y="441"><tspan x="430">Lorem ipsum dolor sit amet, cons ectetuer adipiscing elit,</tspan><tspan x="430" dy="18.7">sed diam nonummy nibh euismod tincidunt ut laoreet</tspan><tspan x="430" dy="18.7">dolore magna aliquam erat volutpat. Ut wisi enim ad minim</tspan><tspan x="430" dy="18.7">veniam, quis nostrud exerci tation ullamcorper suscipit</tspan><tspan x="430" dy="18.7">lobortis nisl ut aliquip ex ea commodo consequat.</tspan></text>
      </g>

      <g font-size="10.5" fill="var(--ink)">
        <rect x="85" y="594" width="6" height="6" fill="var(--yellow)"/><text x="94" y="601">Your text</text>
        <rect x="85" y="609" width="6" height="6" fill="var(--navy)"/><text x="94" y="616">Your text</text>
        <rect x="85" y="624" width="6" height="6" fill="var(--orange)"/><text x="94" y="631">Your text</text>
      </g>

      <polygon class="fill-green" points="0,592 0,608 92,700 108,700"/>
      <polygon class="fill-green" points="14,650 26,650 76,700 64,700"/>
      <polygon class="fill-navy" points="77,648 827,648 872,700 125,700"/>
      <circle cx="684" cy="676" r="14" fill="#1d66a8"/>
      <text x="706" y="684" fill="#1d66a8" font-size="24" font-weight="600">MervoSan</text>
    </svg>
  </section>

  <!-- Contact slide -->
  <section class="slide slide--contact">
    <svg viewBox="0 0 935 700" xmlns="http://www.w3.org/2000/svg">
      <defs>
        <linearGradient id="doctorTone" x1="0" y1="0" x2="0" y2="1">
          <stop offset="0" stop-color="#6a83c0"/>
          <stop offset="1" stop-color="var(--photo-light)"/>
        </linearGradient>
      </defs>
      <rect x="0" y="0" width="366" height="700" fill="url(#doctorTone)" role="img" aria-label="Doctor in a white coat with a stethoscope holding a tablet"/>
      <rect class="fill-navy" x="875" y="0" width="60" height="700"/>
      <circle class="fill-white" cx="366" cy="180" r="68"/>
      <circle class="fill-white" cx="366" cy="350" r="68"/>
      <circle class="fill-white" cx="366" cy="520" r="68"/>
      <text class="fill-white" font-size="82" font-weight="700" letter-spacing="12" transform="translate(168 395) rotate(-90)" text-anchor="middle">THANK YOU</text>

      <path class="icon" d="M340,178 L366,154 L392,178 M346,172v32h40v-32 M358,204v-18h16v18"/>
      <path class="icon" d="M346,330c-6,8 4,30 26,40c8,4 12,-2 14,-6l-8,-8c-3,2-6,3-9,1c-6-4-10-10-12-16c0-3 2-5 4-6l-6-9c-4,0-7,2-9,4z M374,328c6,1 10,6 11,12 M376,318c11,2 18,10 20,22"/>
      <path class="icon" d="M338,504h56v36h-56z M338,504l28,22l28-22 M338,540l20-18 M394,540l-20-18 M348,504v-12h36v12"/>

      <text x="450" y="173" class="heading">Adress</text>
      <text x="450" y="193" class="body-copy">Lorem ipsum dolor sit amet, consectetuer</text>
      <text x="450" y="211" class="body-copy">adipiscing elit, sed diam nonummy nibh</text>
      <text x="450" y="348" class="heading">Phone number</text>
      <text x="450" y="368" class="body-copy">Lorem ipsum dolor sit amet, consectetuer</text>
      <text x="450" y="386" class="body-copy">adipiscing elit, sed diam nonummy nibh</text>
      <text x="450" y="512" class="heading">E-mail</text>
      <text x="450" y="532" class="body-copy">Lorem ipsum dolor sit amet, consectetuer</text>
      <text x="450" y="550" class="body-copy">adipiscing elit, sed diam nonummy nibh</text>
    </svg>
  </section>

</main>
</body>
</html>
```